elearning course template

Our company has a variety of elearning courses. We are currently redesigning the courses and are looking for a new layout for the online learning courses. The layout should be 800x600 and it needs to incorporate the following elements:
1. Course Name
2. Chapter Name
3. Page name
4. Our company logo (see attached file)
5. Navigation bar that includes:
- Next / back buttons
- Page count
- Audio control bar (see attached file)
- Menu items that include: "Menu, Transcript, Resources"
9. Exit button (may be included on the navigation bar if appropriate)
10. Content area must be 775 wide x 442 high

We would like to see designs that use our company colors, blue (RGB 0,69,144) and orange (RGB 222, 111, 51) and dark gray. We're looking for a solution that is clean, crisp and very user friendly. We'd also like to see a little dimension in the layout, we feel that our current layout is very "flat".

You can find out more about our company at www.fernwick-lro.com.

Industry/Entity Type

Graphic Design

```html
<!DOCTYPE html>
<html lang="en">
<head>
<meta charset="utf-8">
<title>Course template – Fernwick LRO</title>
<link rel="stylesheet" href="https://fonts.googleapis.com/css2?family=Questrial&display=swap">
<style>
  :root {
    --brand-blue: #004590;
    --text-dark: #1a1a1a;
    --text-mid: #666666;
    --line-gray: #9a9a9a;
    --icon-gray: #5a5a5a;
    --progress-green: #8cc63f;
    --swoosh-teal: #8fd0dc;
    --swoosh-taupe: #b9ada0;
    --paper: #ffffff;
  }
  * { box-sizing: border-box; margin: 0; padding: 0; }
  html, body {
    width: 1200px; height: 900px; overflow: hidden;
    background: var(--paper);
    font-family: "Questrial", "Century Gothic", sans-serif;
    color: var(--text-dark);
  }
  .frame { position: relative; width: 1200px; height: 900px; overflow: hidden; }

  .backdrop {
    position: absolute; inset: 0;
    background:
      radial-gradient(ellipse 70% 40% at 80% 35%, rgba(143,208,220,.45), transparent 70%),
      radial-gradient(ellipse 60% 25% at 75% 75%, rgba(185,173,160,.35), transparent 70%),
      radial-gradient(ellipse 40% 20% at 5% 60%, rgba(143,208,220,.25), transparent 70%),
      var(--paper);
  }

  .brand {
    position: absolute; left: 20px; top: 14px;
    display: flex; align-items: center; gap: 8px;
    font-size: 22px; color: var(--brand-blue);
  }
  .brand-dot { width: 16px; height: 16px; border-radius: 50%; background: var(--brand-blue); }

  .course-title { position: absolute; left: 17px; top: 70px; font-size: 43px; font-weight: 400; line-height: 1; }
  .chapter-title { position: absolute; left: 17px; top: 121px; font-size: 24px; font-weight: 400; }
  .page-title { position: absolute; right: 18px; top: 129px; font-size: 24px; }

  .tools { position: absolute; right: 17px; top: 16px; display: flex; gap: 18px; }
  .tool { display: flex; flex-direction: column; align-items: center; font-size: 10px; color: var(--text-dark); }
  .tool svg { display: block; margin-bottom: 4px; }

  .content-area {
    position: absolute; left: 18px; top: 163px; width: 1164px; height: 664px;
    border: 1.5px solid var(--line-gray); border-radius: 12px;
    display: flex; flex-direction: column; align-items: center; justify-content: center;
    font-size: 38px; color: var(--text-mid); line-height: 1.25;
  }

  .footer-chapter { position: absolute; left: 17px; top: 830px; font-size: 21px; }
  .page-count { position: absolute; right: 18px; top: 829px; font-size: 21px; }

  .audio-player {
    position: absolute; left: 509px; top: 844px; width: 379px; height: 38px;
    border: 1.5px solid var(--icon-gray); border-radius: 4px; background: var(--paper);
  }
  .audio-pause { position: absolute; left: 12px; top: 13px; }
  .audio-name { position: absolute; left: 38px; top: 6px; font-size: 8px; }
  .audio-time { position: absolute; left: 220px; top: 6px; font-size: 8px; }
  .audio-track {
    position: absolute; left: 38px; top: 20px; width: 217px; height: 6px;
    border: 1px solid var(--line-gray); border-radius: 3px; background: var(--paper);
  }
  .audio-progress { position: absolute; left: 0; top: 0; height: 100%; width: 67%; background: var(--progress-green); border-radius: 3px; }
  .audio-knob, .volume-knob {
    position: absolute; width: 11px; height: 11px; border-radius: 50%;
    background: #e6e6e6; border: 1px solid var(--icon-gray);
  }
  .audio-knob { left: 140px; top: -4px; }
  .audio-volume-icon { position: absolute; left: 274px; top: 12px; }
  .volume-track { position: absolute; left: 298px; top: 18px; width: 64px; height: 4px; background: var(--icon-gray); border-radius: 2px; }
  .volume-knob { left: 44px; top: -4px; }

  .page-nav { position: absolute; left: 902px; top: 845px; display: flex; gap: 10px; }
  .nav-button { display: flex; flex-direction: column; align-items: center; width: 36px; font-size: 6.5px; color: var(--text-mid); white-space: nowrap; }
  .nav-button svg { margin-bottom: 5px; }
</style>
</head>
<body>
<div class="frame">
  <div class="backdrop" role="img" aria-label="Soft sweeping teal and taupe ribbon curves across a white background"></div>

  <div class="brand"><span class="brand-dot"></span>Fernwick LRO</div>

  <h1 class="course-title">Course name</h1>
  <h2 class="chapter-title">Chapter II: Power of you</h2>
  <div class="page-title">Page name</div>

  <nav class="tools">
    <div class="tool">
      <svg width="38" height="40" viewBox="0 0 38 40" aria-hidden="true">
        <g fill="var(--icon-gray)">
          <path d="M4 6 l5-4 l22 24 l3 -1 l3 6 l-5 5 l-6-3 l1-3 z"/>
          <path d="M30 3 a8 8 0 0 0 -9 10 l-17 17 a3 3 0 0 0 5 5 l17-17 a8 8 0 0 0 10-9 l-5 4 l-4-1 l-1-4 z"/>
        </g>
      </svg>MENU
    </div>
    <div class="tool">
      <svg width="28" height="40" viewBox="0 0 28 40" aria-hidden="true">
        <path d="M10 4 h14 v32 h-14" fill="none" stroke="var(--icon-gray)" stroke-width="2"/>
        <path d="M10 4 l8 3 v30 l-8 -1 z" fill="var(--icon-gray)"/>
        <path d="M2 20 h9 m-4 -4 l4 4 l-4 4" fill="none" stroke="var(--icon-gray)" stroke-width="2"/>
      </svg>EXIT
    </div>
  </nav>

  <main class="content-area">
    <span>Content Area</span>
    <span>775 x 442 px</span>
  </main>

  <div class="footer-chapter">Chapter II: Power of you</div>
  <div class="page-count">Page 2/9</div>

  <div class="audio-player">
    <svg class="audio-pause" width="12" height="12" viewBox="0 0 12 12" aria-hidden="true">
      <rect x="1" y="0" width="3.5" height="12" fill="var(--text-dark)"/>
      <rect x="7.5" y="0" width="3.5" height="12" fill="var(--text-dark)"/>
    </svg>
    <span class="audio-name">Audio File Name</span>
    <span class="audio-time">7:34/13.45</span>
    <div class="audio-track"><div class="audio-progress"></div><div class="audio-knob"></div></div>
    <svg class="audio-volume-icon" width="18" height="14" viewBox="0 0 18 14" aria-hidden="true">
      <path d="M1 4 h4 l5-4 v14 l-5-4 h-4 z" fill="var(--text-dark)"/>
      <path d="M12 4 q2 3 0 6 M14 2 q4 5 0 10" fill="none" stroke="var(--text-dark)" stroke-width="1.4"/>
    </svg>
    <div class="volume-track"><div class="volume-knob"></div></div>
  </div>

  <nav class="page-nav">
    <div class="nav-button">
      <svg width="28" height="26" viewBox="0 0 28 26" aria-hidden="true">
        <path d="M1 13 l12-12 v7 h14 v10 h-14 v7 z" fill="var(--icon-gray)"/>
      </svg>Previous page
    </div>
    <div class="nav-button">
      <svg width="28" height="26" viewBox="0 0 28 26" aria-hidden="true">
        <path d="M27 13 l-12-12 v7 h-14 v10 h14 v7 z" fill="var(--icon-gray)"/>
      </svg>Next page
    </div>
  </nav>
</div>
</body>
</html>
```